Cause bitches need love too!

I am creating an ad campaign. It will be a series of featured dogs in our shelter and they will contain a picture of the dog wich should be big enough to see on a yard sign and will change every week. I am placing the signs so that they lead you to the shelter. This is why I am also including the copy that says "you're almost there".

I have 4 tag lines:

1. Find unconditional Love.
2. She'll Love you furever!
3. He'll always listen.
4. Meet your new BFF

You're almost there 318 W Harrowgate Ln
Open 10 - 7/Tues-Sat

The dimensions for the sign are 24" wide and 18" high

Every week we will have a different picture of a different dog (hopefully last week's dog gets adopted). Anyhow, I am printing out yard signs, meaning that instead of printing 160 different signs it would be ideal just to replace the photo. So far the copy that is permanent is: "You're almost there. 318 W. Harrowgate Ln."

I could silhouette the image of the dog as well and super impose it on the sign, that's also a consideration, but ideally if I could have 4 tag lines I could print 40 signs of each and just replace the photo manually each week from my printer that would save costs.
Updates

Not enough designs to chose from and I edited the brief and committed to pay no matter what to increase the amount of designs as per your suggestions.

Target Market(s)

Animal lovers

Industry/Entity Type

Campaign

Font styles to use
Sans Serif

Colors

Designer to choose colors to be used in the design.

Requirements
Must have
• The dimensions for the sign are 24" wide and 18" high
Nice to have
• I want the signs to be hip, they should have a positive feel to them. You can alter the photos if you like. I am even open to new copy if you think something else works better.

```html
<!DOCTYPE html>
<html lang="en">
<head>
<meta charset="utf-8">
<title>Shelter Yard Sign – Find unconditional Love</title>
<link rel="stylesheet" href="https://fonts.googleapis.com/css2?family=Oswald:wght@500;600&display=swap">
<style>
  :root {
    --page-bg: #e9ecef;
    --panel-top: #8c8684;
    --panel-bottom: #b3aeac;
    --headline-yellow: #ffee00;
    --headline-shadow: #1a1a1a;
    --copy-white: #ffffff;
    --copy-black: #111111;
    --band-red: #e3141f;
    --photo-dark: #6f625a;
    --photo-mid: #9a8c83;
    --photo-light: #e6e0dc;
  }
  * { margin: 0; padding: 0; box-sizing: border-box; }
  html, body {
    width: 1200px;
    height: 800px;
    overflow: hidden;
    background: var(--page-bg);
  }
  .yard-sign {
    position: absolute;
    left: 120px;
    top: 40px;
    width: 960px;
    height: 720px;
    overflow: hidden;
    background: linear-gradient(180deg, var(--panel-top) 0%, var(--panel-bottom) 100%);
    font-family: "Oswald", "Arial Narrow", sans-serif;
    box-shadow: 0 6px 24px rgba(0,0,0,0.18);
  }
  .featured-dog-photo {
    position: absolute;
    left: 30px;
    top: 180px;
    width: 620px;
    height: 430px;
    background:
      radial-gradient(ellipse 38% 55% at 45% 55%, var(--photo-light) 0%, var(--photo-mid) 45%, rgba(154,140,131,0) 80%),
      radial-gradient(ellipse 60% 75% at 45% 60%, var(--photo-dark) 0%, rgba(111,98,90,0.6) 55%, rgba(111,98,90,0) 90%);
  }
  .headline {
    position: absolute;
    left: 0;
    top: 0;
    width: 960px;
    height: 340px;
  }
  .headline text {
    font-family: "Oswald", "Arial Narrow", sans-serif;
    font-weight: 600;
    font-size: 66px;
    fill: var(--headline-yellow);
    paint-order: stroke;
    stroke: var(--headline-shadow);
    stroke-width: 3px;
  }
  .directions {
    position: absolute;
    right: 40px;
    top: 345px;
    width: 330px;
    text-align: center;
    line-height: 1.15;
  }
  .directions .almost-there {
    color: var(--copy-white);
    font-weight: 500;
    font-size: 44px;
  }
  .directions .street-number {
    color: var(--copy-black);
    font-weight: 600;
    font-size: 62px;
    line-height: 1.05;
  }
  .directions .street-name {
    color: var(--copy-black);
    font-weight: 500;
    font-size: 46px;
  }
  .hours-band {
    position: absolute;
    left: 0;
    bottom: 0;
    width: 960px;
    height: 110px;
    background: var(--band-red);
    display: flex;
    align-items: center;
    padding-left: 250px;
  }
  .hours-band .hours {
    color: var(--copy-white);
    font-weight: 600;
    font-size: 58px;
    letter-spacing: 0.5px;
  }
</style>
</head>
<body>
  <main class="yard-sign">
    <div class="featured-dog-photo" role="img" aria-label="Photo of this week's featured shelter dog, a grey and white pit bull mix looking up"></div>

    <svg class="headline" viewBox="0 0 960 340" aria-label="Find unconditional Love">
      <defs>
        <path id="headline-arc" d="M 95 150 Q 430 35 880 255"/>
      </defs>
      <text>
        <textPath href="#headline-arc">Find unconditional Love</textPath>
      </text>
    </svg>

    <div class="directions">
      <p class="almost-there">You're almost there</p>
      <p class="street-number">318 W</p>
      <p class="street-name">Harrowgate Ln</p>
    </div>

    <div class="hours-band">
      <p class="hours">Open 10 - 7/Tues-Sat</p>
    </div>
  </main>
</body>
</html>
```